Design a product reviews website

We need a website design and simple logo for the brand Norvique.com. The website will provide reviews of technology products and services. The brand and website should be approachable but should also be trustworthy and high quality. The deliverable should be designs, specs and assets that I can provide to a development team to build the website.

Target Market(s)

People researching products to buy.

Industry/Entity Type

Product

Logo Text

Norvique.com

Number of Pages Required

5+ page

Font styles to use
Sans Serif

Colors
0492cd
0355a3
3176b5
33a6d7
85cae6
85abd2
cedeed
cee9f5

Requirements
Must have
• - Designs for the Homepage, Category and Article pages.
• - Designs for web and mobile.
• - Designs details for the engineering team to use for development.
• - I'm open to other colors than the preferences I chose but I'm more likely to like blues, greys and blacks.

```html
<!DOCTYPE html>
<html lang="en">
<head>
<meta charset="utf-8">
<title>Norvique.com — Product and Service Reviews</title>
<link rel="stylesheet" href="https://fonts.googleapis.com/css2?family=Open+Sans:wght@400;600;700&family=Saira:wght@400;500&display=swap">
<style>
:root{
  --blue-deep:#0355a3;
  --blue-bright:#0492cd;
  --blue-soft:#33a6d7;
  --ink:#444;
  --ink-dark:#333;
  --meta:#9a9a9a;
  --panel:#f0f0f0;
  --header:#f7f7f7;
  --footer:#3a3a3a;
  --rule:#dcdcdc;
}
*{box-sizing:border-box;margin:0;padding:0}
html,body{width:887px;height:1200px;overflow:hidden;background:#fff}
body{position:relative;font-family:"Open Sans",Arial,sans-serif;color:var(--ink)}
.abs{position:absolute}

.site-header{left:0;top:0;width:887px;height:51px;background:var(--header)}
.menu-toggle{left:27px;top:14px;width:27px;height:23px;border-radius:4px;background:#555}
.menu-toggle span{position:absolute;left:5px;width:17px;height:2px;background:#fff;border-radius:1px}
.brand{left:64px;top:10px;font-weight:700;font-size:22px;color:var(--ink-dark);letter-spacing:.2px}
.search{left:534px;top:12px;width:288px;height:27px;background:#fff;border:1px solid #e2e2e2}
.search-btn{right:-1px;top:-1px;width:35px;height:27px;background:var(--blue-bright);display:flex;align-items:center;justify-content:center}

.hero{left:0;top:51px;width:887px;height:221px;background:linear-gradient(110deg,#3c3b3a 0%,#262524 40%,#3a3532 65%,#2a2521 100%)}
.hero-brand{left:0;width:887px;top:80px;text-align:center;font-weight:700;font-size:34px;line-height:44px;color:#fff}
.hero-tagline{left:0;width:887px;top:135px;text-align:center;font-size:13px;line-height:16px;color:#fff}

.section-title{top:290px;font-family:"Saira",Arial,sans-serif;font-weight:400;font-size:20px;letter-spacing:.5px;color:#333}

.category-nav{left:64px;top:323px;width:163px;height:266px;background:var(--panel);padding-top:14px}
.category-nav li{list-style:none;position:relative;height:32px;display:flex;align-items:center;padding-left:23px;font-size:12px;font-weight:600;letter-spacing:.6px;color:#444;border-bottom:1px solid var(--rule)}
.category-nav li:last-child{border-bottom:none;height:30px}
.category-nav li svg{position:absolute;left:10px;top:11px}
.category-nav li.active{background:var(--blue-deep);color:#fff;border-bottom:none;height:28px;margin-bottom:4px}
.category-nav li.active svg{top:9px}
.category-nav li.active::after{content:"";position:absolute;right:0;top:0;width:6px;height:100%;background:var(--blue-bright)}

.photo{display:block}
.post-title{font-weight:700;font-size:16px;letter-spacing:.4px;color:var(--ink)}
.post-meta{font-family:Arial,sans-serif;font-size:9px;color:var(--meta);display:flex;gap:12px;align-items:center}
.post-meta span{display:flex;align-items:center;gap:4px}
.card-title{font-weight:700;font-size:11.5px;line-height:12.8px;letter-spacing:.4px;color:#555}

.popular{left:636px;top:323px;width:188px;height:799px;background:var(--panel)}

.site-footer{left:0;top:1149px;width:887px;height:51px;background:var(--footer);color:#d0d0d0;font-family:Arial,sans-serif;font-size:9.5px;text-align:center;line-height:51px}
</style>
</head>
<body>

<header class="site-header abs">
  <div class="menu-toggle abs"><span style="top:5px"></span><span style="top:10.5px"></span><span style="top:16px"></span></div>
  <div class="brand abs">Norvique.com</div>
  <div class="search abs">
    <div class="search-btn abs">
      <svg width="12" height="12" viewBox="0 0 12 12"><circle cx="5" cy="5" r="3.6" fill="none" stroke="#fff" stroke-width="1.8"/><line x1="7.7" y1="7.7" x2="11" y2="11" stroke="#fff" stroke-width="2"/></svg>
    </div>
  </div>
</header>

<section class="hero abs" role="img" aria-label="Laptop on a wooden desk beside a coffee mug, dimmed">
  <div class="hero-brand abs">Norvique.com</div>
  <p class="hero-tagline abs">The Best Product and Services<br>Reviews and Rankings</p>
</section>

<h2 class="section-title abs" style="left:244px">NEW</h2>
<h2 class="section-title abs" style="left:634px">POPULAR</h2>

<nav>
<ul class="category-nav abs">
  <li class="active"><svg width="6" height="9" viewBox="0 0 6 9"><path d="M1 1l3.5 3.5L1 8" fill="none" stroke="#fff" stroke-width="1.3"/></svg>Home</li>
  <li><svg width="6" height="9" viewBox="0 0 6 9"><path d="M1 1l3.5 3.5L1 8" fill="none" stroke="#777" stroke-width="1"/></svg>Appliances</li>
  <li><svg width="6" height="9" viewBox="0 0 6 9"><path d="M1 1l3.5 3.5L1 8" fill="none" stroke="#777" stroke-width="1"/></svg>Computers</li>
  <li><svg width="6" height="9" viewBox="0 0 6 9"><path d="M1 1l3.5 3.5L1 8" fill="none" stroke="#777" stroke-width="1"/></svg>Electronics</li>
  <li><svg width="6" height="9" viewBox="0 0 6 9"><path d="M1 1l3.5 3.5L1 8" fill="none" stroke="#777" stroke-width="1"/></svg>Home Security</li>
  <li><svg width="6" height="9" viewBox="0 0 6 9"><path d="M1 1l3.5 3.5L1 8" fill="none" stroke="#777" stroke-width="1"/></svg>Mobile</li>
  <li><svg width="6" height="9" viewBox="0 0 6 9"><path d="M1 1l3.5 3.5L1 8" fill="none" stroke="#777" stroke-width="1"/></svg>Smart Home</li>
  <li><svg width="6" height="9" viewBox="0 0 6 9"><path d="M1 1l3.5 3.5L1 8" fill="none" stroke="#777" stroke-width="1"/></svg>Software</li>
</ul>
</nav>

<main>
  <article>
    <div class="photo abs" style="left:246px;top:323px;width:373px;height:223px;background:linear-gradient(160deg,#8a5a32,#c89a66 45%,#a9896a 80%,#7a6a5a)" role="img" aria-label="Wood-panelled kitchen with island and bar stools"></div>
    <h3 class="post-title abs" style="left:246px;top:551px">The Cutest Babies Picture Ever</h3>
    <div class="post-meta abs" style="left:248px;top:580px">
      <span><svg width="8" height="8" viewBox="0 0 8 8"><circle cx="4" cy="2.3" r="2" fill="#aaa"/><path d="M0 8c0-2.5 2-3.5 4-3.5s4 1 4 3.5z" fill="#aaa"/></svg>Posted By: Daniel Arvo</span>
      <span><svg width="9" height="9" viewBox="0 0 9 9"><circle cx="4.5" cy="4.5" r="3.8" fill="none" stroke="#aaa"/><path d="M4.5 2.2v2.5h1.8" fill="none" stroke="#aaa"/></svg>Thursday, May 12, 2016</span>
    </div>
  </article>

  <article>
    <div class="photo abs" style="left:248px;top:622px;width:170px;height:129px;background:linear-gradient(150deg,#4a3020,#8a5632 50%,#5a2a14)" role="img" aria-label="Open dining room with wooden floor"></div>
    <h3 class="card-title abs" style="left:249px;top:757px">Findoro Turns Links Black<br>How To Get Them</h3>
  </article>
  <article>
    <div class="photo abs" style="left:449px;top:622px;width:169px;height:129px;background:linear-gradient(135deg,#f6cfa6,#f2c39a 40%,#4fb3d6 60%,#f5caa0)" role="img" aria-label="Skateboard, camera, sunglasses and phone flat lay"></div>
    <h3 class="card-title abs" style="left:450px;top:757px">Findoro Turns Links Black<br>How To Get Them</h3>
  </article>

  <article>
    <div class="photo abs" style="left:246px;top:811px;width:373px;height:222px;background:linear-gradient(160deg,#d8d2c8,#b89a7a 40%,#eae6e0 65%,#8a6a4a)" role="img" aria-label="Bright white kitchen with dark island and pendant lights"></div>
    <h3 class="post-title abs" style="left:246px;top:1038px">The Cutest Babies Picture Ever</h3>
    <div class="post-meta abs" style="left:248px;top:1064px">
      <span><svg width="8" height="8" viewBox="0 0 8 8"><circle cx="4" cy="2.3" r="2" fill="#aaa"/><path d="M0 8c0-2.5 2-3.5 4-3.5s4 1 4 3.5z" fill="#aaa"/></svg>Posted By: Daniel Arvo</span>
      <span><svg width="9" height="9" viewBox="0 0 9 9"><circle cx="4.5" cy="4.5" r="3.8" fill="none" stroke="#aaa"/><path d="M4.5 2.2v2.5h1.8" fill="none" stroke="#aaa"/></svg>Thursday, May 12, 2016</span>
    </div>
  </article>
</main>

<aside class="popular abs">
  <div class="photo abs" style="left:9px;top:9px;width:170px;height:111px;background:linear-gradient(170deg,#f1d9a0,#d9a860 50%,#9a7040)" role="img" aria-label="Child running with balloons at sunset"></div>
  <h3 class="card-title abs" style="left:9px;top:127px">Findoro Turns Links Black<br>How To Get Them</h3>

  <div class="photo abs" style="left:9px;top:168px;width:170px;height:111px;background:linear-gradient(160deg,#1e1a16,#3a3026 50%,#b8a890)" role="img" aria-label="Dark kitchen with steel ovens"></div>
  <h3 class="card-title abs" style="left:9px;top:286px">Findoro Turns Links Black<br>How To Get Them</h3>

  <div class="photo abs" style="left:9px;top:327px;width:170px;height:111px;background:linear-gradient(160deg,#e8e4dc,#c9c4bc 55%,#c07030)" role="img" aria-label="Kitchen counter with gas hob and pull-out drawer"></div>
  <h3 class="card-title abs" style="left:9px;top:445px">Findoro Turns Links Black<br>How To Get Them</h3>

  <div class="photo abs" style="left:9px;top:486px;width:170px;height:111px;background:linear-gradient(150deg,#9a9ea4,#c8ccd0 50%,#6a6e74)" role="img" aria-label="Rows of stacked washing machines in a laundry room"></div>
  <h3 class="card-title abs" style="left:9px;top:604px">Findoro Turns Links Black<br>How To Get Them</h3>

  <div class="photo abs" style="left:9px;top:645px;width:170px;height:111px;background:linear-gradient(100deg,#d8dce0,#e8e0d8 45%,#3a3a3a 75%,#2a2a2a)" role="img" aria-label="Person placing a dish into a microwave"></div>
  <h3 class="card-title abs" style="left:9px;top:764px">Findoro Turns Links Black<br>How To Get Them</h3>
</aside>

<footer class="site-footer abs">© 2016 Copyright Norvique.com &nbsp;|&nbsp; All Right Reserved</footer>

</body>
</html>
```